ZRD Roofing Billboard Design

Looking for a fresh new billboard design with my new headshot photo and using some info from my previous billboard and maybe website for design/content inspiration. My website is https://zrdroofing.com/

Also attached are my logo and current lawn sign design. I am looking for something simple, clean and modern. The landing page website should be 3816tops.com like my previous billboard has.

```html
<!DOCTYPE html>
<html lang="en">
<head>
<meta charset="utf-8">
<title>ZRD Roofing Billboard</title>
<link rel="stylesheet" href="https://fonts.googleapis.com/css2?family=Montserrat:wght@700&family=Roboto+Slab:wght@500&family=Roboto:wght@700;900&display=swap">
<style>
  :root {
    --navy: #0b2248;
    --lime: #9bb01c;
    --lime-bright: #c4d92e;
    --white: #ffffff;
    --roof-light: #c9ccd0;
    --roof-dark: #6f747a;
    --shirt: #c9d2e6;
    --stage: #eef1f5;
  }
  * { margin: 0; padding: 0; box-sizing: border-box; }
  html, body {
    width: 1200px; height: 840px; overflow: hidden;
    background: var(--stage);
  }
  .billboard {
    position: absolute; left: 0; top: 245px;
    width: 1200px; height: 350px;
    background: var(--white);
    overflow: hidden;
    font-family: "Roboto", Arial, sans-serif;
  }
  .roof-photo {
    position: absolute; left: 430px; top: 0; width: 770px; height: 282px;
    background: linear-gradient(90deg, rgba(255,255,255,1) 0%, rgba(201,204,208,0.7) 22%, var(--roof-light) 40%, var(--roof-dark) 75%, #8d9298 100%);
  }
  .brand {
    position: absolute; left: 26px; top: 28px;
    display: flex; align-items: center; gap: 14px;
  }
  .brand-mark {
    width: 84px; height: 84px; border-radius: 50%;
    background: var(--lime);
    flex: none;
  }
  .brand-name {
    font-family: "Montserrat", Arial, sans-serif; font-weight: 700;
    font-size: 29px; color: var(--navy); line-height: 1;
  }
  .brand-tagline {
    font-family: "Roboto Slab", Georgia, serif; font-weight: 500;
    font-size: 17px; color: var(--navy); margin-top: 8px;
    white-space: nowrap;
  }
  .headline {
    position: absolute; left: 26px; top: 134px;
    font-weight: 900; line-height: 0.92; letter-spacing: -1px;
  }
  .headline .line-1 { display: block; font-size: 60px; color: var(--lime); }
  .headline .line-2 { display: block; font-size: 68px; color: var(--navy); }
  .price-badge {
    position: absolute; left: 462px; top: 26px;
    width: 260px; height: 140px;
    background: var(--navy);
    border-radius: 22px 8px 22px 8px;
    transform: rotate(-4deg);
    text-align: center; padding-top: 14px;
    box-shadow: 3px 4px 0 rgba(0,0,0,0.25);
  }
  .price-label { font-size: 30px; font-weight: 700; color: var(--lime-bright); }
  .price-value {
    font-size: 70px; font-weight: 700; color: var(--white); line-height: 1;
    letter-spacing: -1px;
  }
  .price-value .currency { color: var(--lime-bright); }
  .contact-bar {
    position: absolute; left: 0; bottom: 0; width: 100%; height: 68px;
    background: var(--navy);
    display: flex; align-items: center;
  }
  .phone-tab { width: 80px; height: 68px; flex: none; }
  .phone-number {
    font-size: 53px; font-weight: 700; color: var(--white);
    margin-left: 16px; letter-spacing: -0.5px; white-space: nowrap;
  }
  .landing-url {
    font-size: 46px; font-weight: 700; color: var(--lime-bright);
    margin-left: 16px; letter-spacing: -0.5px; white-space: nowrap;
  }
  .headshot {
    position: absolute; left: 775px; top: 12px;
    width: 385px; height: 338px;
    background: linear-gradient(180deg, #a9b0b8 0%, #b7c0d4 45%, var(--shirt) 100%);
    border-radius: 160px 160px 0 0;
  }
</style>
</head>
<body>
  <main class="billboard">
    <div class="roof-photo" role="img" aria-label="Aerial photo of a newly shingled grey roof"></div>

    <div class="brand">
      <div class="brand-mark"></div>
      <div>
        <div class="brand-name">ZRD Roofing LLC</div>
        <div class="brand-tagline">Built Strong, Built to Last</div>
      </div>
    </div>

    <h1 class="headline">
      <span class="line-1">EXPERT ROOF</span>
      <span class="line-2">REPLACEMENTS</span>
    </h1>

    <div class="price-badge">
      <div class="price-label">Starting at</div>
      <div class="price-value"><span class="currency">$</span>7,499</div>
    </div>

    <div class="contact-bar">
      <svg class="phone-tab" viewBox="0 0 80 68" aria-hidden="true">
        <polygon points="0,0 58,0 80,34 58,68 0,68" fill="#c4d92e"/>
        <path d="M22 20c2-2 5-2 6 0l3 5c1 2 0 3-1 4l-2 2c2 4 5 7 9 9l2-2c1-1 3-2 4-1l5 3c2 1 2 4 0 6l-3 3c-3 2-9 0-15-6s-8-12-6-15z" fill="#0b2248"/>
        <path d="M40 18a12 12 0 0 1 10 10M40 24a6 6 0 0 1 4 4" stroke="#0b2248" stroke-width="2.5" fill="none" stroke-linecap="round"/>
      </svg>
      <span class="phone-number">860·555·0142</span>
      <span class="landing-url">3816Tops.com</span>
    </div>

    <div class="headshot" role="img" aria-label="Headshot of the company owner in a light blue shirt"></div>
  </main>
</body>
</html>
```